UPDATE: I have uploaded the selected logo from the other contest, please use it in your designs.

I have a logo design contest as well so not sure how PixelGuild handles that. They should integrate at some point. I will describe the overall theme with the logo description. See it for details.

The business card side of it would just build on that same theme.

Target Market(s)

8-40

Industry/Entity Type

Business

Contact Information for Business Card

FirstName LastName
Email

Logo Text

Velimor

Font styles to use
Sans Serif

Requirements
Must have
• the url Velimor.com somewhere in it.

```html
<!DOCTYPE html>
<html lang="en">
<head>
<meta charset="utf-8">
<title>Velimor Business Card</title>
<link href="https://fonts.googleapis.com/css2?family=Lato:wght@300;400;700;900&display=swap" rel="stylesheet">
<style>
  :root {
    --stage: #3b3b3d;
    --paper: #ffffff;
    --brand-blue: #1f6fb8;
    --brand-green: #8cc63f;
    --rule-green: #9ccf5a;
    --on-green: #ffffff;
  }
  * { box-sizing: border-box; margin: 0; padding: 0; }
  html, body {
    width: 1200px;
    height: 926px;
    overflow: hidden;
    background: var(--stage);
    font-family: "Lato", sans-serif;
  }
  .sheet {
    width: 1200px;
    height: 926px;
    display: flex;
    flex-direction: column;
    align-items: center;
    justify-content: center;
    gap: 56px;
  }
  .card {
    position: relative;
    width: 630px;
    height: 360px;
    background: var(--paper);
    overflow: hidden;
    box-shadow: 0 10px 30px rgba(0,0,0,0.35);
  }
  /* Front: brand name */
  .card-front {
    display: flex;
    align-items: center;
    justify-content: center;
    gap: 18px;
  }
  .brand-dot {
    width: 34px;
    height: 34px;
    border-radius: 50%;
    background: var(--brand-green);
  }
  .brand-name {
    font-weight: 900;
    font-size: 74px;
    letter-spacing: 10px;
    text-transform: uppercase;
    color: var(--brand-blue);
  }
  /* Back: contact */
  .card-back .identity {
    position: absolute;
    left: 0;
    right: 0;
    top: 78px;
    display: flex;
    flex-direction: column;
    align-items: center;
  }
  .rule {
    width: 330px;
    height: 2px;
    background: var(--rule-green);
  }
  .site {
    margin: 8px 0 2px;
    font-size: 22px;
    font-weight: 400;
    letter-spacing: 1px;
    color: var(--brand-blue);
  }
  .person {
    font-size: 50px;
    line-height: 1;
    letter-spacing: 2px;
    color: var(--brand-blue);
    text-transform: uppercase;
    margin-bottom: 14px;
    white-space: nowrap;
  }
  .person .first { font-weight: 300; }
  .person .last { font-weight: 900; }
  .contact-band {
    position: absolute;
    left: 0;
    right: 0;
    bottom: 0;
    height: 118px;
    background: var(--brand-green);
    display: flex;
    align-items: center;
    justify-content: center;
  }
  .email {
    font-size: 24px;
    font-weight: 700;
    letter-spacing: 1.5px;
    color: var(--on-green);
  }
</style>
</head>
<body>
  <main class="sheet">
    <section class="card card-front">
      <span class="brand-dot"></span>
      <span class="brand-name">Velimor</span>
    </section>

    <section class="card card-back">
      <div class="identity">
        <div class="rule"></div>
        <p class="site">Velimor.com</p>
        <h1 class="person"><span class="first">Dara</span> <span class="last">Quillon</span></h1>
        <div class="rule"></div>
      </div>
      <div class="contact-band">
        <p class="email">daraquillon@Velimor.com</p>
      </div>
    </section>
  </main>
</body>
</html>
```